Private chef located in Ridgehaven, CO

I would like my info located at the top of the landing page, perhaps some Ridgehaven mountain landscapes that I could swap out from summer to winter photos. I need the menu bar to have a link to a blog, about me, photo gallery, recipes & beer reviews. I would also like to have a shop, but only populated with products from quolex or other online retailers that I can affiliate with.
Target Market(s)
Extremely wealthy, affluent people, concierge, international
Number of Pages Required
5+ page

```html
<!DOCTYPE html>
<html lang="en">
<head>
<meta charset="utf-8">
<title>Dorian Castell – Private Chef</title>
<link rel="stylesheet" href="https://fonts.googleapis.com/css2?family=Montserrat:wght@700;800&family=Nunito:wght@800;900&family=Open+Sans:wght@400;600;700&display=swap">
<style>
  :root{
    --orange:#f7901e;
    --orange-deep:#d96a0c;
    --orange-soft:#fbb25c;
    --sky:#b9d2ee;
    --sky-deep:#6f9bd6;
    --ink:#1b1b1b;
    --text:#6a6a6a;
    --muted:#a7a7a7;
    --white:#ffffff;
    --footer:#141414;
  }
  *{box-sizing:border-box;margin:0;padding:0}
  html,body{width:1200px;height:1200px;overflow:hidden;background:var(--white)}
  body{position:relative;font-family:"Open Sans",Arial,sans-serif}
  .page{position:absolute;left:328px;top:55px;width:680px;height:1361px;transform:scale(.8);transform-origin:0 0;background:var(--white);box-shadow:0 0 8px rgba(0,0,0,.18);overflow:hidden}
  .abs{position:absolute}

  .hero{left:0;top:0;width:680px;height:330px;background:linear-gradient(180deg,#a9c8ec 0%,#c9dcf2 40%,#dfe9f6 70%,#ffffff 100%)}
  .peak{left:180px;top:65px;width:380px;height:260px;background:radial-gradient(ellipse at 50% 55%,#5e86c0 0%,#8eb0dc 45%,rgba(255,255,255,0) 72%)}
  .nav{left:0;top:0;width:680px;height:50px;background:rgba(214,230,248,.75);border-bottom:1px solid rgba(255,255,255,.6)}
  .nav-link{top:20px;font-size:8px;color:var(--white);letter-spacing:.2px;text-transform:uppercase}
  .nav-link.active{color:var(--orange);font-weight:700}
  .cart{left:486px;top:20px}
  .call-btn{left:526px;top:15px;width:58px;height:17px;border-radius:9px;background:var(--orange);color:var(--white);font-size:6.5px;font-weight:700;text-align:center;line-height:17px}
  .hero-title{left:0;top:75px;width:680px;text-align:center;font-family:"Montserrat",Arial,sans-serif;font-weight:800;font-size:50px;line-height:48px;color:var(--white);text-shadow:2px 3px 0 var(--orange)}
  .avatar{left:290px;top:196px;width:100px;height:100px;border-radius:50%;border:3px solid var(--orange);background:linear-gradient(135deg,#3c3a3a,#8a7060 60%,#c9a48a)}

  .h2{font-family:"Nunito",Arial,sans-serif;font-weight:900;font-size:22px;color:var(--orange)}
  .center{left:0;width:680px;text-align:center}
  .rule{left:334px;width:12px;height:1px;background:var(--orange)}
  .about-text{left:137px;top:340px;width:262px;font-size:7.6px;line-height:12.7px;color:var(--text)}
  .feature-icon{width:42px;height:42px;border-radius:50%;background:linear-gradient(135deg,var(--orange),var(--orange-deep))}
  .feature-title{font-size:7.6px;font-weight:600;color:var(--ink)}
  .feature-text{font-size:7.4px;line-height:12.8px;color:var(--text);width:160px}

  .svc{top:533px;width:94px;height:120px}
  .svc-label{left:0;bottom:5px;width:94px;text-align:center;color:var(--white);font-weight:700;font-size:8px;line-height:10.5px}
  .svc-frame{left:6px;top:6px;width:82px;height:108px;border:1px solid var(--white)}
  .btn{height:20px;border-radius:10px;background:linear-gradient(90deg,var(--orange-deep),var(--orange));color:var(--white);font-size:8px;font-weight:700;line-height:20px}

  .gallery-bg{left:0;top:770px;width:680px;height:300px;background:linear-gradient(180deg,#ffffff 0%,#e6ebf1 35%,#eef1f5 70%,#ffffff 100%)}
  .photo{box-shadow:0 2px 6px rgba(0,0,0,.25)}

  .review{top:1099px;width:128px;height:107px;background:var(--white);border-radius:4px;box-shadow:0 0 5px rgba(247,144,30,.55);text-align:center;padding:24px 9px 0}
  .review-name{font-size:6px;font-weight:700;color:var(--ink);margin-bottom:7px}
  .review-text{font-size:5.5px;line-height:8.5px;color:var(--muted)}
  .review-avatar{top:1078px;width:36px;height:36px;border-radius:50%;border:2px solid var(--white)}

  .contacts{left:0;top:1238px;width:680px;height:94px;background:var(--orange)}
  .field{top:1299px;width:94px;height:16px;border-radius:8px;background:var(--white);font-size:6px;color:#555;padding-left:10px;line-height:16px}
  .send{left:449px;top:1299px;width:93px;height:16px;border-radius:8px;border:1px solid var(--white);color:var(--white);font-size:6px;font-weight:700;text-align:center;line-height:14px}
  .footer{left:0;top:1332px;width:680px;height:29px;background:var(--footer);color:#d8d8d8;font-size:6px;text-align:center;line-height:32px}
</style>
</head>
<body>
<main class="page">
  <div class="abs hero" role="img" aria-label="Snowy mountain peak rising above clouds under a blue sky"></div>
  <div class="abs peak"></div>

  <nav class="abs nav">
    <span class="abs nav-link active" style="left:149px">About me</span>
    <span class="abs nav-link" style="left:212px">Gallery</span>
    <span class="abs nav-link" style="left:266px">Recipes</span>
    <span class="abs nav-link" style="left:317px">Beer reviews</span>
    <span class="abs nav-link" style="left:393px">Blog</span>
    <span class="abs nav-link" style="left:434px">Contact</span>
    <svg class="abs cart" width="10" height="9" viewBox="0 0 10 9"><path d="M0 1h2l1.3 4.5h5L9.5 2H2.6" fill="none" stroke="#fff" stroke-width="1.2"/><circle cx="3.8" cy="7.6" r=".9" fill="#fff"/><circle cx="7.8" cy="7.6" r=".9" fill="#fff"/></svg>
    <span class="abs call-btn">CALL US</span>
  </nav>

  <h1 class="abs hero-title">DORIAN<br>CASTELL</h1>
  <div class="abs avatar" role="img" aria-label="Portrait photo of the chef"></div>

  <h2 class="abs h2" style="left:137px;top:302px">About Me</h2>
  <p class="abs about-text">Sed ut perspiciatis unde omnis iste natus error sit voluptatem accusantium doloremque laudantium, totam rem aperiam, eaque ipsa quae ab illo inventore veritatis et quasi architecto beatae vitae dicta sunt explicabo. Nemo enim ipsam voluptatem quia voluptas sit aspernatur aut odit aut fugit, sed quia consequuntur magni</p>

  <div class="abs feature-icon" style="left:414px;top:308px">
    <svg width="42" height="42" viewBox="0 0 42 42" fill="none" stroke="#fff" stroke-width="1.3"><path d="M14 20a5 5 0 0 1 3-9 6 6 0 0 1 10 1 4.5 4.5 0 0 1 1 8.5V29H15v-9z"/><path d="M15 25h13"/></svg>
  </div>
  <div class="abs feature-title" style="left:469px;top:310px">BEST CUISINE</div>
  <div class="abs feature-text" style="left:469px;top:322px">Lorem Ipsum is simply dummy text of the printing and typesetting industry</div>

  <div class="abs feature-icon" style="left:414px;top:364px">
    <svg width="42" height="42" viewBox="0 0 42 42" fill="none" stroke="#fff" stroke-width="1.3"><path d="M13 21h16a8 8 0 0 1-16 0z"/><path d="M16 28l-3 6M26 28l3 6M21 29v5"/><path d="M17 12c1 1.5-1 2.5 0 4M21 12c1 1.5-1 2.5 0 4M25 12c1 1.5-1 2.5 0 4"/></svg>
  </div>
  <div class="abs feature-title" style="left:469px;top:368px">SPECIAL EVENT CATERING</div>
  <div class="abs feature-text" style="left:469px;top:380px">Lorem Ipsum is simply dummy text of the printing and typesetting industry</div>

  <h2 class="abs h2 center" style="top:464px">My Services</h2>
  <div class="abs rule" style="top:505px"></div>

  <div class="abs svc" style="left:106px;background:linear-gradient(180deg,#d9b08a,#f2a24a 60%,#f7901e)" role="img" aria-label="Hand sprinkling seasoning over a dish">
    <span class="abs svc-label">STOWMATE<br>MEALS</span></div>
  <div class="abs svc" style="left:231px;background:linear-gradient(180deg,#e58b2c,#f2a146 55%,#f28a1a)" role="img" aria-label="Trays of catered food">
    <div class="abs svc-frame"></div><span class="abs svc-label" style="bottom:54px">CATERING</span></div>
  <div class="abs svc" style="left:354px;background:linear-gradient(180deg,#f4ede6,#e88a4e 55%,#f7901e)" role="img" aria-label="Chef slicing tomatoes on a board">
    <span class="abs svc-label">FULL TIME<br>CHEF</span></div>
  <div class="abs svc" style="left:479px;background:linear-gradient(180deg,#efe2d4,#e7a36a 50%,#f7901e)" role="img" aria-label="Chef plating a dish with tweezers">
    <span class="abs svc-label">PERSONAL<br>CHEF</span></div>

  <div class="abs btn" style="left:293px;top:675px;width:93px;padding-left:18px">View all
    <svg class="abs" style="left:78px;top:6px" width="6" height="8" viewBox="0 0 6 8"><path d="M1 1l3.5 3L1 7" fill="none" stroke="#fff" stroke-width="1.2"/></svg></div>

  <div class="abs gallery-bg" role="img" aria-label="Faint snowy mountain range"></div>
  <h2 class="abs h2 center" style="top:740px">Gallery</h2>
  <div class="abs rule" style="top:781px"></div>

  <div class="abs photo" style="left:414px;top:795px;width:127px;height:119px;background:linear-gradient(135deg,#3a3a3a,#c9a36a 45%,#e7d2c9 75%,#b06a4a)" role="img" aria-label="Plated seafood dish with red onion"></div>
  <div class="abs photo" style="left:137px;top:845px;width:128px;height:119px;background:linear-gradient(135deg,#8a6a4a,#d7c3a8 40%,#9a7a58 70%,#6a4a3a)" role="img" aria-label="Roasted meat with sauce on a plate"></div>
  <div class="abs photo" style="left:241px;top:811px;width:197px;height:127px;background:linear-gradient(135deg,#2a2422,#6b4a3a 40%,#9fb07a 65%,#e8e6e2)" role="img" aria-label="Steak with asparagus and red pepper garnish"></div>

  <div class="abs btn" style="left:449px;top:943px;width:92px;text-align:center">View all</div>

  <h2 class="abs h2 center" style="top:1017px">Reviews</h2>
  <div class="abs rule" style="top:1058px"></div>

  <div class="abs review" style="left:137px">
    <div class="review-name">THEO MARSH</div>
    <div class="review-text">Chef Dorian was professional and fun to visit with as he prepared our meal. The meal was prepared on time and it was amazing! I strongly recommend Chef Dorian when you are in Ridgehaven</div>
  </div>
  <div class="abs review" style="left:276px">
    <div class="review-name">LENA FORDE</div>
    <div class="review-text">Great food and great guy!</div>
  </div>
  <div class="abs review" style="left:414px">
    <div class="review-name">INES VARGA</div>
    <div class="review-text">Lorem Ipsum is simply dummy text of the printing and typesetting industry.</div>
  </div>
  <div class="abs review-avatar" style="left:183px;background:linear-gradient(135deg,#3a5a6a,#c9a47a)" role="img" aria-label="Reviewer portrait"></div>
  <div class="abs review-avatar" style="left:321px;background:linear-gradient(135deg,#8fb0d6,#c98a7a)" role="img" aria-label="Reviewer portrait"></div>
  <div class="abs review-avatar" style="left:459px;background:linear-gradient(135deg,#2e3a3e,#7a8a8a)" role="img" aria-label="Reviewer portrait"></div>

  <section class="abs contacts"></section>
  <h2 class="abs h2 center" style="top:1251px;color:var(--white)">Contacts</h2>
  <div class="abs field" style="left:137px">Name</div>
  <div class="abs field" style="left:241px">E-mail</div>
  <div class="abs field" style="left:344px">Phone</div>
  <div class="abs send">SEND</div>

  <footer class="abs footer">Copyrights 2019. All rights reserved</footer>
</main>
</body>
</html>
```